Wine Label for a Prosecco Wine Called Tavi

Prosecco is a white sparkling wine from Italy. We are looking for an eye catching, elegant label for this prosecco that is called "Tavi" because it is a young, fresh, lively white sparkling wine. (We do not want to see children or babies featured on the label-- just the name TAVI please.) Attached is the old label for your reference, and the bottle type that will be used , which is a dark green Burgundy style bottle (pls ignore the label on the bottle). Please no grapes or wine glasses on the label. We are looking for something: eye catching / fun / ELEGANT (not cheap). We would be happy with a fun color too. Remember-- elegant, eye catching! Thanks!
Updates

Hi All, I think I made a mistake in my brief and have updated it. I also uploaded a competitor's label that we like very much to give better direction to what we are looking for. Also, the word Tavi cannot be vertical, nor can it be broken. It needs to read: TAVI or Tavi. Thanks

Target Market(s)

American adults male and female.

Colors
abd036
33a6d7
33b8a4
ffcf3e

Requirements
Must have
• The mandatory information as shown on old labels. The word TAVI should be very prominent.
Nice to have
• The uploaded photo of a competitor's prosecco shows a label we really like... if you could play around with this shape and style we'd be very happy.
Should not have
• No grape images, no wine glass images, no images of babies or children.

```html
<!DOCTYPE html>
<html lang="it">
<head>
<meta charset="utf-8">
<title>Tavi Frizzante – label colourways</title>
<link href="https://fonts.googleapis.com/css2?family=Poppins:wght@300;400;600&family=Playfair+Display:wght@400;700&display=swap" rel="stylesheet">
<style>
  :root {
    --teal: #33b8a4;
    --green: #abd036;
    --blue: #33a6d7;
    --yellow: #ffcf3e;
    --ink: #ffffff;
    --backdrop: #000000;
  }
  html, body {
    margin: 0;
    padding: 0;
    width: 887px;
    height: 1200px;
    overflow: hidden;
    background: var(--backdrop);
  }
  .sheet {
    position: relative;
    width: 887px;
    height: 1200px;
  }
  .label {
    position: absolute;
    width: 372px;
    height: 518px;
    background: var(--bg);
    color: var(--ink);
  }
  .label--a { left: 57px;  top: 64px;  --bg: var(--teal);  --accent: var(--green); }
  .label--b { left: 462px; top: 64px;  --bg: var(--green); --accent: var(--teal); }
  .label--c { left: 57px;  top: 623px; --bg: var(--green); --accent: var(--yellow); }
  .label--d { left: 462px; top: 622px; --bg: var(--blue);  --accent: var(--green); }

  .designation {
    position: absolute;
    left: 224px;
    top: 48px;
    margin: 0;
    font-family: "Poppins", sans-serif;
    font-weight: 300;
    font-size: 16.5px;
    line-height: 25.7px;
    letter-spacing: 0.2px;
  }
  .style-name {
    position: absolute;
    left: 226px;
    top: 129px;
    margin: 0;
    font-family: "Playfair Display", serif;
    font-weight: 700;
    font-size: 21px;
    letter-spacing: 0.4px;
    line-height: 1;
  }
  .style-dot {
    position: absolute;
    left: 321px;
    top: 154px;
    width: 17px;
    height: 14px;
    background: var(--accent);
  }
  .region {
    position: absolute;
    left: 62px;
    top: 340px;
    margin: 0;
    font-family: "Playfair Display", serif;
    font-weight: 400;
    font-size: 16.5px;
    line-height: 1;
  }
  .brand-mark {
    position: absolute;
    left: 62px;
    top: 380px;
    width: 46px;
    height: 46px;
    background: var(--accent);
  }
  .brand-name {
    position: absolute;
    left: 122px;
    top: 362px;
    margin: 0;
    font-family: "Poppins", sans-serif;
    font-weight: 600;
    font-size: 74px;
    line-height: 1;
    letter-spacing: -1px;
  }
  .wine-type {
    position: absolute;
    left: 62px;
    top: 451px;
    margin: 0;
    font-family: "Poppins", sans-serif;
    font-weight: 400;
    font-size: 12.5px;
    letter-spacing: 1.6px;
    line-height: 1;
  }
</style>
</head>
<body>
<main class="sheet">
  <section class="label label--a">
    <p class="designation">Indicazione<br>Geografica<br>Tipica</p>
    <p class="style-name">FRIZZANTE</p>
    <span class="style-dot"></span>
    <p class="region">Veneto</p>
    <span class="brand-mark"></span>
    <h1 class="brand-name">Tavi</h1>
    <p class="wine-type">PROSECCO</p>
  </section>

  <section class="label label--b">
    <p class="designation">Indicazione<br>Geografica<br>Tipica</p>
    <p class="style-name">FRIZZANTE</p>
    <span class="style-dot"></span>
    <p class="region">Veneto</p>
    <span class="brand-mark"></span>
    <h1 class="brand-name">Tavi</h1>
    <p class="wine-type">PROSECCO</p>
  </section>

  <section class="label label--c">
    <p class="designation">Indicazione<br>Geografica<br>Tipica</p>
    <p class="style-name">FRIZZANTE</p>
    <span class="style-dot"></span>
    <p class="region">Veneto</p>
    <span class="brand-mark"></span>
    <h1 class="brand-name">Tavi</h1>
    <p class="wine-type">PROSECCO</p>
  </section>

  <section class="label label--d">
    <p class="designation">Indicazione<br>Geografica<br>Tipica</p>
    <p class="style-name">FRIZZANTE</p>
    <span class="style-dot"></span>
    <p class="region">Veneto</p>
    <span class="brand-mark"></span>
    <h1 class="brand-name">Tavi</h1>
    <p class="wine-type">PROSECCO</p>
  </section>
</main>
</body>
</html>
```